Tiny Petal Product Label for Tear-Free Head-to-Toe Wash

Need a bottle label design for a new line of natural products targeting infants and children. Products are Pediatrician-developed and paraben-free, sulfate-free, fragrance-free, and cruelty-free. Design should be clean and have a high-end feel to it. Will need other product labels in Tiny Petal line designed as well in upcoming projects.

Target Market(s)

Newborn to young elementary age children and their parents

Industry/Entity Type

Cosmetics/Beauty

Font styles to use
Other font styles liked:
• Brand fonts are Jost and Sonorous

Colors

Designer to choose colors to be used in the design.

Requirements
Must have
• Tiny Petal logo, Pediatrician Developed logo, and a clean high-end feel to it. The label must fit the specialty bottle we will be using (label measurements and diagram will be provided) for the front and back of bottle only (NOT the side labels). It must include our list of ingredients (will provide once designer selected).
Nice to have
• Should stand out on the shelf of other baby products due to it's clean simplicity and high-end feel
Should not have
• too much of a "kiddie" feel to it (targeting the parents not the kids)

```html
<!DOCTYPE html>
<html lang="en">
<head>
<meta charset="utf-8">
<title>Tiny Petal – Tear-Free Head-to-Toe Wash Labels</title>
<link href="https://fonts.googleapis.com/css2?family=Jost:wght@300;400;500&display=swap" rel="stylesheet">
<style>
  :root {
    --backdrop: #dce8f6;
    --label: #ffffff;
    --ink: #262626;
    --ink-soft: #4a4a4a;
    --gold: #8c6b2c;
    --amber: #b5791c;
  }
  * { box-sizing: border-box; margin: 0; padding: 0; }
  html, body { width: 1200px; height: 1200px; overflow: hidden; }
  body {
    background: var(--backdrop);
    font-family: "Jost", Arial, sans-serif;
    color: var(--ink);
    display: flex;
    align-items: center;
    justify-content: center;
    gap: 70px;
  }
  .label {
    width: 480px;
    height: 760px;
    background: var(--label);
    border-radius: 120px 120px 28px 28px;
    box-shadow: 0 10px 40px rgba(60, 90, 130, 0.12);
    display: flex;
    flex-direction: column;
    align-items: center;
    text-align: center;
    padding: 70px 44px 50px;
  }
  .brand {
    display: flex;
    align-items: center;
    gap: 12px;
    font-size: 26px;
    font-weight: 400;
    letter-spacing: 0.12em;
    text-transform: uppercase;
    color: var(--ink);
  }
  .brand-dot {
    width: 20px; height: 20px;
    border-radius: 50%;
    border: 2px solid var(--ink);
  }
  .kicker {
    margin-top: 56px;
    font-size: 15px;
    letter-spacing: 0.08em;
    color: var(--ink-soft);
  }
  .title {
    font-size: 40px;
    font-weight: 400;
    line-height: 1.05;
    letter-spacing: 0.01em;
  }
  .band {
    margin-top: 6px;
    background: var(--gold);
    color: #fff;
    font-size: 15px;
    letter-spacing: 0.6em;
    padding: 3px 8px 3px 18px;
  }
  .scent {
    margin-top: 30px;
    font-size: 16px;
    letter-spacing: 0.1em;
    line-height: 1.35;
  }
  .claims {
    list-style: none;
    margin-top: 30px;
    font-size: 15px;
    color: var(--amber);
    line-height: 1.45;
    text-align: left;
  }
  .claims li::before { content: "• "; }
  .badge {
    margin-top: 44px;
    width: 76px; height: 76px;
    border-radius: 50%;
    background: #e7e7e7;
  }
  .volume {
    margin-top: auto;
    font-size: 15px;
    color: var(--ink-soft);
    letter-spacing: 0.03em;
  }
  .section-head {
    margin-top: 30px;
    font-size: 14px;
    font-weight: 500;
  }
  .copy {
    margin-top: 6px;
    font-size: 12.5px;
    font-weight: 300;
    line-height: 1.5;
    color: var(--ink-soft);
  }
  .net {
    margin-top: 36px;
    font-size: 17px;
    color: var(--amber);
    letter-spacing: 0.03em;
  }
  .origin-badge {
    margin-top: auto;
    width: 70px; height: 28px;
    background: #e4e4e4;
  }
</style>
</head>
<body>
  <section class="label label-front" aria-label="Front label">
    <div class="brand"><span class="brand-dot"></span>Tiny Petal</div>
    <p class="kicker">TEAR-FREE</p>
    <h1 class="title">HEAD-TO-TOE</h1>
    <span class="band">WASH</span>
    <p class="scent">Lavender<br>&amp; Argan Oil</p>
    <ul class="claims">
      <li>Paraben-Free</li>
      <li>Cruelty-Free</li>
      <li>Sulfate-Free</li>
      <li>Fragrance-Free</li>
    </ul>
    <div class="badge" role="img" aria-label="Pediatrician developed badge"></div>
    <p class="volume">300ml 10.fl. oz</p>
  </section>

  <section class="label label-back" aria-label="Back label">
    <div class="brand"><span class="brand-dot"></span>Tiny Petal</div>
    <p class="kicker">TEAR-FREE</p>
    <h2 class="title">HEAD-TO-TOE</h2>
    <span class="band">WASH</span>
    <p class="section-head">Ingredients:</p>
    <p class="copy">Lorem Ipsum, Lorem Ipsum, Lorem Ipsum, Lorem Ipsum, Lorem Ipsum, Lorem Ipsum, Lorem Ipsum, Lorem Ipsum, Lorem Ipsum, Lorem Ipsum.</p>
    <p class="section-head">Instructions:</p>
    <p class="copy">when an unknown printer took a galley of type and scrambled it to make a type specimen book. It has survived not only five centuries, but also the leap into electronic typesetting, remaining essentially unchanged. It was popularised like Folio Layout including versions of Lorem Ipsum.</p>
    <p class="net">Net Vol.:&nbsp; 300ml</p>
    <div class="origin-badge" role="img" aria-label="Country of origin badge"></div>
  </section>
</body>
</html>
```